TLB Feedback sticker

We need a sticker design for our secondary school (aged 11 - 18). This is to allow teachers to provide feedback to students and vice-versa, having a conversation with the learner. I would love to have at least two different designs and it to be attractive, so that all can be included. I've attached the basic outline with the information to be presented. It should be A5 size, so that 2 of these can be fitted in.

Target Market(s)

Secondary school students

Industry/Entity Type

School

Font styles to use
Sans Serif

Requirements
Must have
• Attached details of the headings and enough space for all parties to respond.
Should not have
• Anything deemed inappropriate for secondary students

```html
<!DOCTYPE html>
<html lang="en">
<head>
<meta charset="utf-8">
<title>Formative Feedback Sticker</title>
<link href="https://fonts.googleapis.com/css2?family=Arimo:wght@400;600;700&display=swap" rel="stylesheet">
<style>
  :root {
    --wood-light: #c98a4a;
    --wood-mid: #b06e33;
    --wood-dark: #8f5424;
    --frame: #c9894e;
    --frame-edge: #a8672f;
    --paper: #ffffff;
    --rule: #c9c8e6;
    --divider: #9d9d9d;
    --spine: #5c5c5c;
    --tab: #7a4512;
    --tab-text: #ffffff;
    --ink: #1a1a1a;
  }
  html, body {
    margin: 0;
    padding: 0;
    overflow: hidden;
  }
  .canvas {
    position: relative;
    width: 1200px;
    height: 846px;
    overflow: hidden;
    font-family: "Arimo", Arial, sans-serif;
    color: var(--ink);
  }
  .wood-backdrop {
    position: absolute;
    inset: 0;
    background: linear-gradient(100deg, var(--wood-mid) 0%, var(--wood-light) 35%, var(--wood-mid) 65%, var(--wood-dark) 100%);
  }
  .title-tab {
    position: absolute;
    left: 765px;
    top: 62px;
    width: 316px;
    height: 50px;
    background: var(--tab);
    color: var(--tab-text);
    font-weight: 700;
    font-size: 22px;
    letter-spacing: 0.5px;
    display: flex;
    align-items: center;
    justify-content: center;
    box-shadow: 0 2px 4px rgba(0,0,0,0.35);
  }
  .notebook {
    position: absolute;
    left: 72px;
    top: 117px;
    width: 1055px;
    height: 678px;
    background: var(--frame);
    border: 2px solid var(--frame-edge);
    border-radius: 40px;
    box-sizing: border-box;
    box-shadow: 0 3px 6px rgba(0,0,0,0.3);
  }
  .spread {
    position: absolute;
    left: 88px;
    top: 129px;
    width: 1023px;
    height: 652px;
    background: var(--paper);
    border-radius: 34px;
    overflow: hidden;
  }
  .rules {
    position: absolute;
    left: 0;
    right: 0;
    top: 64px;
    height: 580px;
    background-image: repeating-linear-gradient(to bottom, transparent 0, transparent 22px, var(--rule) 22px, var(--rule) 23.3px);
  }
  .spine {
    position: absolute;
    left: 511px;
    top: 0;
    width: 2px;
    height: 100%;
    background: var(--spine);
  }
  .label {
    position: absolute;
    font-size: 15px;
    font-weight: 600;
    white-space: nowrap;
    background: var(--paper);
    padding-right: 4px;
  }
  .tick {
    position: absolute;
    width: 18px;
    height: 18px;
  }
  .divider {
    position: absolute;
    height: 4px;
    background: var(--divider);
  }
</style>
</head>
<body>
<div class="canvas">
  <div class="wood-backdrop" role="img" aria-label="Warm wooden plank surface"></div>

  <div class="notebook"></div>

  <div class="spread">
    <div class="rules"></div>
    <div class="spine"></div>

    <!-- Left page -->
    <div class="label" style="left:36px; top:98px;">Strengths (What Went Well…)</div>
    <svg class="tick" style="left:36px; top:119px;" viewBox="0 0 18 18"><circle cx="8" cy="10" r="6" fill="none" stroke="#222" stroke-width="1.4"/><path d="M4.5 10 L7.5 13 L15 3" fill="none" stroke="#222" stroke-width="1.8" stroke-linecap="round"/></svg>
    <svg class="tick" style="left:36px; top:167px;" viewBox="0 0 18 18"><circle cx="8" cy="10" r="6" fill="none" stroke="#222" stroke-width="1.4"/><path d="M4.5 10 L7.5 13 L15 3" fill="none" stroke="#222" stroke-width="1.8" stroke-linecap="round"/></svg>
    <svg class="tick" style="left:36px; top:215px;" viewBox="0 0 18 18"><circle cx="8" cy="10" r="6" fill="none" stroke="#222" stroke-width="1.4"/><path d="M4.5 10 L7.5 13 L15 3" fill="none" stroke="#222" stroke-width="1.8" stroke-linecap="round"/></svg>

    <div class="divider" style="left:33px; top:269px; width:247px;"></div>
    <div class="divider" style="left:286px; top:269px; width:200px;"></div>
    <div class="label" style="left:36px; top:292px;">Target (Even Better If…)</div>

    <div class="divider" style="left:33px; top:417px; width:247px;"></div>
    <div class="divider" style="left:286px; top:417px; width:200px;"></div>
    <div class="label" style="left:36px; top:438px;">Action</div>

    <!-- Right page -->
    <div class="label" style="left:748px; top:43px; padding:0;">Date : _______________________</div>
    <div class="label" style="left:540px; top:98px;">Response (from the student):</div>
    <div class="divider" style="left:540px; top:341px; width:450px;"></div>
    <div class="label" style="left:540px; top:361px;">Response and reflection (from the teacher):</div>
  </div>

  <div class="title-tab">FORMATIVE FEEDBACK</div>
</div>
</body>
</html>
```